Family owned plumbing contractor needs eye catching business card design

Business cards that are unique, eye catching, and provide customers with general company information, such as name, address, phone number, website, employee name/title, cell phone #, & email address. We are transitioning to a new logo that utilizes a more retro feel, so we are interested in seeing some cool old school designs in the mix. We are liking the dark background on some of the samples on this website. If that is workable with our artwork, we would like to see that incorporated into the design.
Contact Information for Business Card
Copperline Pipeworks, Inc.
www.copperlinepipeworks.example
(555) 392-7068 phone
Nevada License #64205
California License #5810473
Dale Wrennick, President
(555) 618-9032 cell
dale@copperlinepipeworks.example
Residential * Commercial * Service
Requirements
Must have
- The business card details listed above & logo provided.
Nice to have
- I made some notes about color options in the description.

```html
<!DOCTYPE html>
<html lang="en">
<head>
<meta charset="utf-8">
<title>Copperline Pipeworks, Inc. — Business Card</title>
<link rel="stylesheet" href="https://fonts.googleapis.com/css2?family=Montserrat:wght@400;500;600;700&display=swap">
<style>
  :root {
    --slate: #58798f;
    --slate-dark: #45637a;
    --teal: #6cc3b2;
    --paper: #ffffff;
    --stage: #e9e9e7;
    --ink: #4d6d85;
  }
  * { margin: 0; padding: 0; box-sizing: border-box; }
  html, body { width: 1200px; height: 831px; overflow: hidden; }
  body {
    background: var(--stage);
    font-family: "Montserrat", Arial, sans-serif;
    position: relative;
  }
  .card {
    position: absolute;
    width: 520px;
    height: 297px;
    top: 267px;
    overflow: hidden;
    box-shadow: 0 6px 18px rgba(0,0,0,0.18);
  }
  .card-back { left: 50px; background: var(--slate); }
  .card-front { left: 630px; background: var(--paper); }
  .texture {
    position: absolute; inset: 0;
    background: radial-gradient(ellipse at 40% 35%, #6a8aa0 0%, var(--slate) 55%, var(--slate-dark) 100%);
  }
  .back-mark {
    position: absolute; left: 50%; top: 50%;
    transform: translate(-50%, -50%);
    width: 290px; height: 180px;
    border-radius: 50%;
    background: var(--paper);
    border: 5px solid var(--teal);
    display: flex; align-items: center; justify-content: center;
    text-align: center;
  }
  .brand-name {
    font-weight: 700;
    color: var(--ink);
    line-height: 1.2;
  }
  .back-mark .brand-name { font-size: 22px; width: 200px; }
  .front-art { position: absolute; left: 0; top: 0; }
  .front-mark {
    position: absolute; left: 30px; top: 40px;
    width: 190px;
    display: flex; align-items: center; gap: 10px;
  }
  .front-mark .dot {
    width: 20px; height: 20px; border-radius: 50%;
    background: var(--teal); flex: none;
  }
  .front-mark .brand-name { font-size: 17px; }
  .licenses {
    position: absolute; left: 30px; top: 150px;
    font-size: 12px; color: var(--ink); line-height: 1.5;
  }
  .person {
    position: absolute; right: 14px; top: 36px;
    text-align: right; color: var(--paper);
    white-space: nowrap;
  }
  .person .name { font-size: 14px; font-weight: 600; letter-spacing: 0.5px; text-transform: uppercase; line-height: 1.3; }
  .person .title { font-size: 11px; font-weight: 500; }
  .contact {
    position: absolute; right: 62px; top: 178px;
    text-align: right; font-size: 12px; font-weight: 500;
    color: var(--ink); line-height: 1.4;
    white-space: nowrap;
  }
  .services {
    position: absolute; left: 0; right: 0; bottom: 0; height: 38px;
    background: var(--teal);
    color: var(--paper);
    font-size: 13px; font-weight: 500; letter-spacing: 0.8px;
    display: flex; align-items: center; padding-left: 150px;
  }
</style>
</head>
<body>

<section class="card card-back">
  <div class="texture" role="img" aria-label="Distressed crackle texture in slate blue"></div>
  <div class="back-mark">
    <span class="brand-name">Copperline Pipeworks, Inc.</span>
  </div>
</section>

<section class="card card-front">
  <svg class="front-art" width="520" height="259" viewBox="0 0 520 259">
    <path d="M150,0 C300,0 490,80 512,259 L520,259 L520,0 Z" fill="#58798f"/>
    <path d="M150,0 C300,0 490,80 512,259" fill="none" stroke="#6cc3b2" stroke-width="5"/>
  </svg>

  <div class="front-mark">
    <span class="dot"></span>
    <span class="brand-name">Copperline Pipeworks, Inc.</span>
  </div>

  <div class="licenses">
    <p>Nevada License #64205</p>
    <p>California License #5810473</p>
  </div>

  <div class="person">
    <p class="name">Dale Wrennick</p>
    <p class="title">President</p>
  </div>

  <div class="contact">
    <p>P: (555) 392-7068</p>
    <p>C: (555) 618-9032</p>
    <p>dale@copperlinepipeworks.example</p>
    <p>www.copperlinepipeworks.example</p>
  </div>

  <div class="services">Residential • Commercial • Service</div>
</section>

</body>
</html>
```